Veracor Systems
Business Cards
Veracor Systems - Information Technology
Creative Brief
Professional
Martin Osgood
Vice President
Veracor IT Systems Harbourline Tower 482 Dunmore Ave East,Suite 3100 Toronto ON, M4R 2T7
martin.osgood@veracorsystems-example.ca
www.veracorsystems-example.ca

```html
<!DOCTYPE html>
<html lang="en">
<head>
<meta charset="utf-8">
<title>Veracor Systems – Business Card</title>
<link rel="stylesheet" href="https://fonts.googleapis.com/css2?family=Open+Sans:wght@400;600;700&display=swap">
<style>
  :root {
    --backdrop: #1b1b1d;
    --card: #ffffff;
    --ink: #2a2a2a;
    --brand: #1f73bd;
    --brand-deep: #0c3f7c;
    --brand-light: #6fb3e6;
  }
  html, body {
    margin: 0;
    width: 1200px;
    height: 787px;
    overflow: hidden;
    background: var(--backdrop);
    font-family: "Open Sans", Arial, sans-serif;
  }
  .card {
    position: absolute;
    left: 110px;
    top: 110px;
    width: 984px;
    height: 600px;
    background: var(--card);
    border-radius: 26px;
    overflow: hidden;
    color: var(--ink);
  }
  .card__swoosh {
    position: absolute;
    inset: 0;
  }
  .brand {
    position: absolute;
    left: 70px;
    top: 58px;
    display: flex;
    align-items: center;
    gap: 18px;
  }
  .brand__square {
    width: 96px;
    height: 96px;
    background: var(--brand);
  }
  .brand__name {
    font-size: 46px;
    font-weight: 700;
    color: var(--brand);
    line-height: 1;
    letter-spacing: 1px;
  }
  .brand__tagline {
    position: absolute;
    left: 184px;
    top: 160px;
    font-size: 10px;
    letter-spacing: 0.4px;
    color: var(--ink);
    text-transform: uppercase;
  }
  .person {
    position: absolute;
    right: 52px;
    top: 210px;
    text-align: right;
  }
  .person__name {
    font-size: 36px;
    font-weight: 700;
    color: var(--brand-deep);
    line-height: 1.2;
  }
  .person__title {
    font-size: 22px;
    line-height: 1.4;
  }
  .address {
    position: absolute;
    left: 70px;
    top: 262px;
    font-size: 24px;
    line-height: 35px;
  }
  .contact {
    position: absolute;
    left: 70px;
    top: 448px;
    font-size: 22px;
    line-height: 35px;
  }
  .contact__label {
    color: var(--brand);
    font-weight: 700;
  }
  .website {
    position: absolute;
    left: 70px;
    top: 540px;
    font-size: 24px;
    letter-spacing: 2px;
  }
  .website__domain { color: var(--brand); }
</style>
</head>
<body>
  <section class="card">
    <svg class="card__swoosh" width="984" height="600" viewBox="0 0 984 600" aria-hidden="true">
      <defs>
        <linearGradient id="swooshBlue" x1="0" y1="0" x2="1" y2="1">
          <stop offset="0" stop-color="#3f93d6"/>
          <stop offset="1" stop-color="#0c3f7c"/>
        </linearGradient>
      </defs>
      <path d="M890 0 C1010 150 990 420 600 600 L984 600 L984 0 Z" fill="var(--brand-light)"/>
      <path d="M915 0 C1030 160 1000 430 640 600 L984 600 L984 0 Z" fill="url(#swooshBlue)"/>
      <path d="M960 120 C990 300 900 470 720 600 L984 600 L984 120 Z" fill="var(--brand-deep)" opacity="0.55"/>
    </svg>

    <div class="brand">
      <div class="brand__square"></div>
      <div class="brand__name">VERACOR SYSTEMS</div>
    </div>
    <div class="brand__tagline">Enterprise IT service and solution for small and medium business</div>

    <div class="person">
      <div class="person__name">Martin Osgood</div>
      <div class="person__title">Vice President</div>
    </div>

    <div class="address">
      Veracor IT Systems<br>
      Harbourline Tower<br>
      482 Dunmore Ave East,Suite 3100<br>
      Toronto ON,<br>
      M4R 2T7
    </div>

    <div class="contact">
      <span class="contact__label">P :</span> 1 (416) 555-0148<br>
      <span class="contact__label">E :</span> martin.osgood@veracorsystems-example.ca
    </div>

    <div class="website">www.<span class="website__domain">veracorsystems-example</span>.ca</div>
  </section>
</body>
</html>
```